Business Card That Looks Like a Sports Card

Want it to look like a sports trading card. That front should have a baseball player. The back will list our contact info and website info etc.

Contact Information for Business Card

www.ridgecrestathletics.example
visitRCX.example
Email: marcus@ridgecrestathletics.example

Colors

Designer to choose colors to be used in the design.

Requirements
Must have
• Use our current logo and color scheme. Must look like a sports trading card.

```html
<!DOCTYPE html>
<html lang="en">
<head>
<meta charset="utf-8">
<title>Ridgecrest Athletics – Business Card</title>
<link href="https://fonts.googleapis.com/css2?family=Lato:wght@400;700&display=swap" rel="stylesheet">
<style>
  :root {
    --backdrop: #5c5c5c;
    --card: #0b090a;
    --edge: #1f5fa3;
    --accent-blue: #1d5fae;
    --accent-teal: #3bb594;
    --text-light: #c9cbcf;
    --text-muted: #a9acb1;
    --divider: #1c2c44;
    --figure-light: #b9bcc0;
    --figure-dark: #8e9196;
  }
  * { box-sizing: border-box; margin: 0; padding: 0; }
  html, body { width: 1200px; height: 900px; overflow: hidden; }
  body {
    background: var(--backdrop);
    font-family: "Lato", sans-serif;
    display: flex;
    align-items: center;
    justify-content: center;
    gap: 48px;
  }
  .card {
    width: 540px;
    height: 310px;
    background: var(--card);
    border: 1.5px solid var(--edge);
    position: relative;
    overflow: hidden;
  }
  /* Contact side */
  .card--contact {
    display: flex;
    align-items: stretch;
  }
  .brand {
    width: 46%;
    display: flex;
    flex-direction: column;
    align-items: center;
    justify-content: center;
    gap: 14px;
  }
  .brand__mark {
    width: 44px;
    height: 44px;
    border-radius: 50%;
    background: var(--accent-teal);
  }
  .brand__name {
    color: var(--accent-teal);
    font-weight: 700;
    font-size: 24px;
    letter-spacing: 1px;
    text-align: center;
    line-height: 1.2;
    text-transform: uppercase;
  }
  .divider {
    width: 1px;
    margin: 40px 0;
    background: var(--divider);
  }
  .details {
    flex: 1;
    padding: 40px 22px 0 26px;
    color: var(--text-light);
  }
  .details__name {
    color: var(--accent-blue);
    font-weight: 700;
    font-size: 25px;
    line-height: 1.1;
  }
  .details__title {
    color: var(--text-muted);
    font-size: 14px;
    margin-top: 4px;
  }
  .details__address {
    font-size: 13px;
    line-height: 1.45;
    margin-top: 22px;
  }
  .contact-list {
    list-style: none;
    margin-top: 10px;
    font-size: 12.5px;
    line-height: 1.75;
  }
  .contact-list li {
    display: flex;
    align-items: center;
    gap: 8px;
    white-space: nowrap;
  }
  .contact-list svg { width: 12px; height: 12px; flex: none; }
  /* Front side */
  .card--front {
    display: flex;
    align-items: center;
    justify-content: center;
  }
  .player-art {
    width: 190px;
    height: 180px;
    border-radius: 6px;
    background: radial-gradient(ellipse at center, var(--figure-light) 0%, var(--figure-dark) 70%, #3a3b3e 100%);
    opacity: 0.9;
  }
</style>
</head>
<body>
  <section class="card card--contact">
    <div class="brand">
      <span class="brand__mark"></span>
      <span class="brand__name">Ridgecrest<br>Athletics</span>
    </div>
    <div class="divider"></div>
    <div class="details">
      <h1 class="details__name">Daniel Reyes</h1>
      <p class="details__title">Founder &amp; CEO</p>
      <p class="details__address">4820 Summit Field Road, Suite 300,<br>Ridgecrest, Ohio 45000</p>
      <ul class="contact-list">
        <li>
          <svg viewBox="0 0 12 12" aria-hidden="true"><path d="M2.5 1h2l1 2.6-1.3 1a6.5 6.5 0 0 0 3.2 3.2l1-1.3 2.6 1v2A1.2 1.2 0 0 1 9.8 11 9 9 0 0 1 1 2.2 1.2 1.2 0 0 1 2.5 1z" fill="var(--accent-blue)"/></svg>
          +1 555 014 0000
        </li>
        <li>
          <svg viewBox="0 0 12 12" aria-hidden="true"><rect x="0.5" y="2" width="11" height="8" rx="1" fill="var(--accent-blue)"/><path d="M1 2.5 6 6.5l5-4" stroke="var(--card)" stroke-width="1" fill="none"/></svg>
          marcus@ridgecrestathletics.example
        </li>
        <li>
          <svg viewBox="0 0 12 12" aria-hidden="true"><circle cx="6" cy="6" r="5" fill="none" stroke="var(--accent-blue)" stroke-width="1.2"/><path d="M1 6h10M6 1c-2.4 2.8-2.4 7.2 0 10M6 1c2.4 2.8 2.4 7.2 0 10" stroke="var(--accent-blue)" stroke-width="0.9" fill="none"/></svg>
          www.ridgecrestathletics.example
        </li>
      </ul>
    </div>
  </section>

  <section class="card card--front">
    <div class="player-art" role="img" aria-label="Light grey silhouette illustration of a baseball batter mid-swing"></div>
  </section>
</body>
</html>
```